Pelverhook LLC
Business Cards & Stationary
Professional
Tobias Wendell
President
482 Orchard Crest Road
Dunmore Falls, NJ 07934-2718
tobias.wendell@mailvexo.com
www.pelverhook.com
I require the full suite of stationary products i.e.:- Business card, letterhead, envelope, fax cover sheet, thank you cards, invoice etc.
Just the logo on the back of the card.

```html
<!DOCTYPE html>
<html lang="en">
<head>
<meta charset="utf-8">
<title>Pelverhook LLC — Business Card</title>
<link rel="stylesheet" href="https://fonts.googleapis.com/css2?family=Marcellus+SC&family=Cinzel:wght@600&display=swap">
<style>
  :root {
    --canvas: #e4e5e7;
    --silver-light: #fbfbfb;
    --silver-mid: #e3e4e6;
    --silver-dark: #c9cbce;
    --blue-deep: #1d3f9a;
    --blue-mid: #2f6bd1;
    --blue-light: #5aa8ec;
    --rule-dark: #1a2433;
    --brand-blue: #245a96;
    --mark-fill: #3e5f95;
    --text-light: #ffffff;
    --shadow: rgba(0, 0, 0, 0.28);
  }
  * { margin: 0; padding: 0; box-sizing: border-box; }
  html, body {
    width: 1200px;
    height: 919px;
    overflow: hidden;
    background: var(--canvas);
  }
  .stage { position: relative; width: 1200px; height: 919px; }

  .card {
    position: absolute;
    width: 753px;
    height: 435px;
    border-radius: 20px;
    overflow: hidden;
    box-shadow: 0 10px 26px var(--shadow);
    background: linear-gradient(180deg, var(--silver-light) 0%, var(--silver-mid) 60%, var(--silver-dark) 100%);
  }
  .card--front { left: 37px; top: 28px; z-index: 2; }
  .card--back  { left: 410px; top: 470px; z-index: 1; }

  /* brand lock-up */
  .brand {
    position: absolute;
    display: flex;
    flex-direction: column;
    align-items: center;
  }
  .brand__mark {
    border-radius: 50%;
    background: var(--mark-fill);
  }
  .brand__name {
    font-family: "Cinzel", serif;
    font-weight: 600;
    color: var(--brand-blue);
    letter-spacing: 0.02em;
    white-space: nowrap;
  }
  .card--front .brand { left: 0; width: 610px; top: 30px; }
  .card--front .brand__mark { width: 88px; height: 88px; }
  .card--front .brand__name { font-size: 40px; margin-top: 10px; }

  .card--back .brand { left: 0; right: 0; top: 100px; }
  .card--back .brand__mark { width: 108px; height: 108px; }
  .card--back .brand__name { font-size: 48px; margin-top: 14px; }

  /* front lower band */
  .band {
    position: absolute;
    left: 0; right: 0; top: 0; bottom: 0;
  }
  .band svg { display: block; }

  .identity {
    position: absolute;
    left: 40px;
    width: 340px;
    top: 268px;
    text-align: right;
    color: var(--text-light);
    font-family: "Marcellus SC", serif;
  }
  .identity__name { font-size: 30px; line-height: 1.1; }
  .identity__title { font-size: 26px; line-height: 1.15; margin-bottom: 8px; }
  .identity__address { font-size: 19px; line-height: 1.2; }

  .divider {
    position: absolute;
    left: 382px;
    top: 272px;
    width: 1px;
    height: 125px;
    background: rgba(255, 255, 255, 0.6);
  }

  .contact {
    position: absolute;
    left: 405px;
    top: 272px;
    color: var(--text-light);
    font-family: "Marcellus SC", serif;
    font-size: 17px;
    line-height: 1.3;
  }
  .contact__web { margin-top: 16px; }
</style>
</head>
<body>
<main class="stage">

  <section class="card card--front" aria-label="Business card front">
    <div class="band">
      <svg width="753" height="435" viewBox="0 0 753 435" aria-hidden="true">
        <defs>
          <linearGradient id="bandBlue" x1="0" y1="0" x2="1" y2="0">
            <stop offset="0" stop-color="var(--blue-light)"/>
            <stop offset="0.45" stop-color="var(--blue-mid)"/>
            <stop offset="1" stop-color="var(--blue-deep)"/>
          </linearGradient>
        </defs>
        <path d="M0 232 H180 L196 206 L212 232 H753 V435 H0 Z" fill="var(--rule-dark)"/>
        <path d="M0 242 H182 L196 219 L210 242 H753 V435 H0 Z" fill="url(#bandBlue)"/>
      </svg>
    </div>

    <div class="brand">
      <div class="brand__mark" aria-hidden="true"></div>
      <div class="brand__name">Pelverhook LLC</div>
    </div>

    <div class="identity">
      <div class="identity__name">Tobias Wendell</div>
      <div class="identity__title">President</div>
      <div class="identity__address">482 Orchard Crest Road</div>
      <div class="identity__address">Dunmore Falls, NJ 07934-2718</div>
    </div>

    <div class="divider" aria-hidden="true"></div>

    <div class="contact">
      <div>P: 201.555.0142</div>
      <div>C: 201.555.0187</div>
      <div>F: 201.555.0142</div>
      <div>E: tobias.wendell@mailvexo.com</div>
      <div class="contact__web">www.pelverhook.com</div>
    </div>
  </section>

  <section class="card card--back" aria-label="Business card back">
    <div class="brand">
      <div class="brand__mark" aria-hidden="true"></div>
      <div class="brand__name">Pelverhook LLC</div>
    </div>
  </section>

</main>
</body>
</html>
```